BRIGHT COLORFUL + 55 FAMILY HISTORY BROCHURE 11 x 17 bifold

11 x 17 Bifold Flyer I have given you the Layout I just need you to make it Pretty

YOU DO NOT NEED TO FOLLOW MY LAYOUT, You can but dont have too

Target Market(s)

55 year old consumers, who could choose our service of Hereditary Cancer Screening

Industry/Entity Type

Health And Wellness

Requirements
Must have
• Must be appealing to Grand Parents, must make them want to test , show lots of pictures of grand children, YOU DO NOT NEED TO FOLLOW MY LAYOUT , You can but dont have too
Nice to have
• use our colors of our logo , YOU DO NOT NEED TO FOLLOW MY LAYOUT , You can but dont have too
Should not have
• YOU DO NOT NEED TO FOLLOW MY LAYOUT, You can but dont have too

```html
<!DOCTYPE html>
<html lang="en">
<head>
<meta charset="utf-8">
<title>Hereditary Cancer Screening Brochure</title>
<link href="https://fonts.googleapis.com/css2?family=Righteous&family=Montserrat:wght@300;400;600&display=swap" rel="stylesheet">
<style>
:root{
  --green:#a6c96a;
  --green-deep:#7fa83f;
  --navy:#1f2549;
  --slate:#6f7472;
  --teal:#5bb5a8;
  --ink:#3d3d3d;
  --body:#6a6a6a;
  --white:#ffffff;
  --display:'Righteous',sans-serif;
  --text:'Montserrat',sans-serif;
}
*{margin:0;padding:0;box-sizing:border-box}
html,body{width:1200px;height:1200px;overflow:hidden;background:var(--white)}
body{position:relative;font-family:var(--text)}
.page{position:absolute;overflow:hidden}
.dots{position:absolute;left:0;top:0;width:100%;height:100%}
.abs{position:absolute}
.para{font-size:6.8px;line-height:8.8px;font-weight:300;text-align:justify;text-align-last:center}

/* cover spread */
.cover{left:29px;top:30px;width:788px;height:556px;background:var(--green)}
.cover-photo{left:0;top:0;width:393px;height:556px;
  background:linear-gradient(180deg,#8fbf3a 0%,#6f9a34 35%,#7a7a4a 70%,#9c9684 100%)}
.cover-title{left:30px;top:30px;font-family:var(--display);color:var(--white);font-size:23px;line-height:34px;letter-spacing:.5px;text-transform:uppercase}
.cover-intro{left:263px;top:30px;width:110px;color:var(--white);font-size:6.4px;line-height:8.6px;font-weight:300;text-align:justify;text-align-last:center}
.brand{font-family:var(--text);font-weight:400;text-transform:uppercase;font-size:7px;line-height:7.6px;display:flex;align-items:center;gap:4px}
.brand .mark{width:16px;height:16px;border-radius:50%;flex:none}
.brand-light{color:var(--white)}
.brand-light .mark{background:var(--white);opacity:.9}
.cover-question{left:411px;top:101px;color:var(--white);font-size:6.6px;line-height:9px}
.cover-question strong{font-weight:600;text-transform:none}
.cover-question span{font-weight:300}
.cover-headline{left:411px;top:136px;font-family:var(--display);font-size:21px;color:var(--white);text-transform:uppercase;letter-spacing:.5px}
.cover-headline .accent{color:var(--navy)}
.cover-body{left:411px;top:180px;width:292px;color:var(--white);font-size:6.6px;line-height:8.8px;font-weight:300}
.cover-body p+p{margin-top:7px}
.cover-url{left:428px;top:504px;color:var(--white);font-size:6.6px;font-weight:300}

/* inside page */
.inside{left:386px;top:614px;width:787px;height:556px;background:var(--white)}
.brand-dark{color:var(--navy)}
.brand-dark .mark{background:var(--green)}
.rule{position:absolute;width:1px;background:var(--green)}
.text-col{color:var(--body)}
.benefits-title{left:30px;top:259px;font-family:var(--display);font-size:20px;line-height:25px;color:var(--ink);text-transform:uppercase;letter-spacing:.5px}
.benefits-title .accent{color:var(--green)}
.benefits-quote{left:29px;top:340px;font-size:6.6px;color:var(--ink);font-weight:300}
.highlight{color:var(--green-deep)}
.step-num{font-family:var(--text);font-weight:300;font-size:38px;color:var(--ink);line-height:1}
.family-photo{left:394px;top:166px;width:334px;height:223px;
  background:linear-gradient(135deg,#e9ecea 0%,#d8dcd6 40%,#c9b6a4 70%,#7d9a6e 100%)}
</style>
</head>
<body>

<section class="page cover">
  <div class="abs cover-photo" role="img" aria-label="Photograph of a grandfather sitting on a stone wall in a sunlit park with two young grandchildren"></div>
  <h1 class="abs cover-title">Hereditary<br>Cancer<br>Screening</h1>
  <p class="abs cover-intro">There are many known risk factors for cancer. Genetics and family history are often overlooked.</p>
  <div class="abs brand brand-light" style="left:304px;top:94px"><span class="mark"></span><span>Kinwell<br>Health<br>Group</span></div>

  <svg class="dots" viewBox="0 0 788 556" aria-hidden="true">
    <circle cx="661" cy="58" r="8" fill="var(--slate)"/>
    <circle cx="488" cy="304" r="10.5" fill="var(--navy)"/>
    <circle cx="713" cy="275" r="5" fill="var(--teal)"/>
    <circle cx="692" cy="355" r="4" fill="var(--teal)"/>
    <circle cx="445" cy="395" r="8.5" fill="#5f8f9a"/>
    <circle cx="621" cy="422" r="7.5" fill="var(--navy)"/>
  </svg>

  <p class="abs cover-question"><strong>DOES CANCER Run In Your Family?</strong><br><span>A Simple Swab Could SAVE a Family Members LIFE</span></p>
  <h2 class="abs cover-headline">Get <span class="accent">Tested</span> Today</h2>
  <div class="abs cover-body">
    <p>Your decision won't just affect you, it will also impact your family, since your test results may forecast their cancer risks, too.</p>
    <p>We believe it is important to understand what can and cannot be learned with genetic testing. Genetic mutations can increase risks for certain cancers, but this does not mean cancer will definitely develop. You should be prepared to receive positive or negative results. Most people receive negative results meaning no mutations associated with an increased risk for the hereditary cancers.</p>
  </div>
  <p class="abs cover-url">www.kinwellscreening.com</p>
  <div class="abs brand brand-light" style="left:703px;top:494px"><span class="mark"></span><span>Kinwell<br>Health<br>Group</span></div>
</section>

<section class="page inside">
  <svg class="dots" viewBox="0 0 787 556" aria-hidden="true">
    <circle cx="28" cy="18" r="5.5" fill="var(--ink)"/>
    <text x="28" y="20.3" font-size="6" fill="#fff" text-anchor="middle" font-family="Montserrat,sans-serif">1</text>
    <circle cx="99" cy="61" r="12" fill="var(--navy)"/>
    <circle cx="256" cy="73" r="12" fill="var(--green)"/>
    <circle cx="86" cy="96" r="2.5" fill="var(--green)"/>
    <circle cx="62" cy="117" r="8" fill="var(--navy)"/>
    <circle cx="119" cy="143" r="6" fill="var(--green)"/>
    <circle cx="66" cy="174" r="18.5" fill="var(--navy)"/>
    <circle cx="284" cy="293" r="8" fill="var(--navy)"/>
    <circle cx="66" cy="429" r="18.5" fill="var(--green)"/>
    <circle cx="752" cy="21" r="6" fill="var(--green)"/>
    <circle cx="178" cy="524" r="4" fill="var(--navy)"/>
    <circle cx="213" cy="524" r="5" fill="var(--green)"/>
    <circle cx="248" cy="524" r="7.5" fill="var(--navy)"/>
    <circle cx="284" cy="524" r="8" fill="var(--green)"/>
    <circle cx="318" cy="524" r="10.5" fill="var(--navy)"/>
    <circle cx="354" cy="524" r="15" fill="var(--green)"/>
    <circle cx="430" cy="524" r="15" fill="var(--navy)"/>
    <circle cx="466" cy="524" r="10.5" fill="var(--green)"/>
    <circle cx="501" cy="524" r="8" fill="var(--navy)"/>
    <circle cx="536" cy="524" r="7.5" fill="var(--green)"/>
    <circle cx="572" cy="524" r="5" fill="var(--navy)"/>
    <circle cx="608" cy="524" r="4" fill="var(--green)"/>
  </svg>

  <div class="abs brand brand-dark" style="left:325px;top:15px"><span class="mark"></span><span>Kinwell<br>Health<br>Group</span></div>

  <div class="abs text-col para" style="left:141px;top:112px;width:219px">
    <p>Genetic Testing is done to determine whether family members without obvious illness have inherited the same mutation as a family member who is known to carry a cancer associated mutation. Meaning Will You Help Your Kids &amp; Grand Children</p>
    <p style="margin-top:4px">There are many benefits to getting tested, regardless of the eventual result. If one of your family members however distant had cancer, there is a chance that you inherited a gene mutation that not only increases your personal risk of cancer, but also could be passed to the next generation. Those who are carriers of hereditary cancer gene mutations, could be at risk of getting cancer earlier in life than the general population. The sooner genetic testing is done, the more likely it is that the risk can be managed appropriately.</p>
  </div>
  <span class="rule" style="left:374px;top:112px;height:124px"></span>

  <h2 class="abs benefits-title">What are<br>the benefits<br>of <span class="accent">testing ?</span></h2>
  <p class="abs benefits-quote">"The Power of Knowledge"</p>

  <span class="rule" style="left:141px;top:350px;height:137px"></span>
  <div class="abs text-col para" style="left:153px;top:350px;width:222px">
    <p>Helping Younger Family Members Know if there is a Risk and Preparing for it. Knowing if you have a genetic mutation is that you can work with your doctor to monitor and address your cancer risks. According to the National Cancer Council eating 5 or more servings of vegetables, fruits and Most Importantly also lowering your intake of red meat, dairy and eggs will help prevent or delay cancer.</p>
    <p style="margin-top:12px"><span class="highlight">My father had genetic testing and found he had hereditary nonpolyposis colorectal cancer (HNPCC)</span> commonly known as Lynch syndrome. My name is Margaret Cole and I am a 10-year survivor of colorectal cancer. From an early age I learned the importance of screenings and knew about signs and symptoms. Following screening guidelines for individuals at an increased risk &amp; Knowing my family history saved my life!</p>
  </div>

  <span class="rule" style="left:412px;top:34px;height:102px"></span>
  <div class="abs text-col para" style="left:428px;top:34px;width:293px">
    <p>Genetic testing revealed Daniel Marsh carried a mutation that gave him a 55 to 70 percent chance of developing stomach cancer. Early screening revealed there were 14 sites of stage 1A cancer. Once the news sunk in, he realized his Mother Genetic Testing Saved His Life.</p>
    <p style="margin-top:11px">Genetic Testing Saved My Life, Because of my age and Ashkenazi Jewish ancestry, my Dr recommended genetic testing and they were right. I had the BRCA Gene, because of this my other two sister got tested, my younger sister was positive and my older sister was negative. Now we are in control, there are steps that can be taken to reduce the risks, including enhanced breast cancer screening, risk reducing surgeries, and chemoprevention, in which drugs are used to try to reduce the risk or delay the development of cancer.</p>
  </div>
  <span class="abs step-num" style="left:748px;top:40px">1</span>
  <span class="abs step-num" style="left:741px;top:97px">2</span>

  <div class="abs family-photo" role="img" aria-label="Photograph of smiling grandparents on a sofa hugged by their two grandchildren"></div>
  <span class="rule" style="left:750px;top:166px;height:223px"></span>

  <span class="abs step-num" style="left:420px;top:430px">3</span>
  <div class="abs text-col para" style="left:458px;top:410px;width:274px">
    <p>A breast cancer survivor before age 30: 'Genetic testing saved my life' Nora Halden was diagnosed with breast cancer two weeks before her 29th birthday. Halden, now 30, credits her recovery to awareness of a hereditary genetic mutation that predisposed her and her family to the disease. After my mom tested positive for the BRCA 1 gene mutation, I knew genetic testing was something that I would need. Once I tested positive, I was referred to a breast health clinic for increased surveillance. There, my medical care providers were very diligent in making sure I was watched closely. Knowledge is power and, in this case, Genetic testing saved my life!</p>
  </div>
  <span class="rule" style="left:750px;top:410px;height:72px"></span>
</section>

</body>
</html>
```